BUSINESS CARD MIRELLE KOSVIK

I need a new business card for my personal business.
I am a Naturopath and Nutritionist working doing private consults in the health and wellness arena.
I would like to see designs that are, clean minimalist but colourful.
I like:
White (clean,fresh, minimalist)
pops of one colour ONLY.Choose a colour to run with and keep it simple.
green
light blue
mustard
Bright yellow
Charcoal
The final design should communicate professionalism but also be in touch with nature.
Key Information to include:
MIRELLE KOSVIK
ABN 41 582 307 916
PTRQB 872310
Tel 0491 738 624
NATUROPATH | HERBALIST | NUTRITON CONSULTANT
BHSc (Naturopathic Studies) Grad Dip (Naturopathy)
BACK OF CARD : YOUR NEXT APPOINTMENT ..................................
I already have a logo (picture attached)But I would be more than happy to NOT have this included. I am very Open to cards WITHOUT current logo/ ones that weave the colour of my logo but do not use the logo.
I have included pictures attached to give examples of the styles/colors I enjoy.
Updates
I have added a picture of a mortar and pestle - one just like this would be lovely to include in your entry.
TIA

```html
<!DOCTYPE html>
<html lang="en">
<head>
<meta charset="utf-8">
<title>Mirelle Kosvik — Appointment Card</title>
<link rel="stylesheet" href="https://fonts.googleapis.com/css2?family=Open+Sans:wght@300;400&display=swap">
<style>
  :root {
    --paper: #ffffff;
    --accent: #4a8c3a;
    --edge: #1a1a1a;
  }
  html, body {
    margin: 0;
    padding: 0;
    width: 1200px;
    height: 731px;
    overflow: hidden;
    background: var(--paper);
  }
  .card {
    position: relative;
    box-sizing: border-box;
    width: 1200px;
    height: 731px;
    border: 1px solid var(--edge);
    background: var(--paper);
    color: var(--accent);
    font-family: "Open Sans", "Segoe UI", sans-serif;
    font-weight: 300;
    text-align: center;
  }
  p { margin: 0; }
  .practitioner-name {
    position: absolute;
    top: 34px;
    left: 0;
    right: 0;
    font-size: 34px;
    line-height: 46px;
    font-weight: 400;
    letter-spacing: 6px;
  }
  .credentials {
    position: absolute;
    top: 108px;
    left: 0;
    right: 0;
    font-size: 42px;
    line-height: 55px;
  }
  .registration {
    position: absolute;
    top: 323px;
    left: 0;
    right: 0;
    font-size: 40px;
    line-height: 54px;
  }
  .appointment {
    position: absolute;
    top: 538px;
    left: 0;
    right: 0;
    font-size: 42px;
    line-height: 56px;
  }
  .appointment-line {
    display: block;
    width: 502px;
    margin: 34px auto 0;
    border-bottom: 3px dotted var(--accent);
  }
</style>
</head>
<body>
  <main class="card">
    <p class="practitioner-name">MIRELLE KOSVIK</p>
    <section class="credentials">
      <p class="roles">NATUROPATH | HERBALIST | NUTRITON CONSULTANT</p>
      <p class="qualifications">BHSc (Naturopathic Studies) Grad Dip (Naturopathy)</p>
    </section>
    <section class="registration">
      <p class="member-number">PTRQB 872310</p>
      <p class="abn">ABN 41 582 307 916</p>
      <p class="phone">Tel 0491 738 624</p>
    </section>
    <section class="appointment">
      <p class="appointment-label">Your Next Appointment At:</p>
      <span class="appointment-line"></span>
    </section>
  </main>
</body>
</html>
```